Security camera surveillance warning Sign

Security Camera Sign 11" x 11" Red, Yellow and Black (White Background)
I would like a line drawing of camera image attached.
Wording: All Suspicious or Criminal Activity Will Be Reported!
WARNING
24 HOUR SURVEILLANCE

Industry/Entity Type

Security

Colors
ec1f27
000000
ffc214

Requirements
Nice to have
• I uploaded a sign and would like the new design look something like that

```html
<!DOCTYPE html>
<html lang="en">
<head>
<meta charset="utf-8">
<title>24 Hour Surveillance Warning Sign</title>
<link rel="stylesheet" href="https://fonts.googleapis.com/css2?family=Roboto:wght@700;900&display=swap">
<style>
  :root {
    --sign-red: #ec1f27;
    --sign-yellow: #ffc214;
    --sign-black: #000000;
    --sign-white: #ffffff;
    --camera-dark: #141414;
    --camera-light: #5a5a5a;
  }
  html, body {
    margin: 0;
    padding: 0;
    width: 1200px;
    height: 1198px;
    overflow: hidden;
    background: var(--sign-white);
  }
  .sign {
    display: block;
    width: 1200px;
    height: 1198px;
  }
  .sign text {
    font-family: "Roboto", "Arial", sans-serif;
  }
  .header-band-edge { fill: var(--sign-red); }
  .header-band { fill: var(--sign-yellow); }
  .header-title { fill: var(--sign-black); font-weight: 900; font-size: 152px; }
  .footer-band { fill: var(--sign-black); }
  .badge-halo { fill: var(--sign-white); }
  .badge-ring { fill: var(--sign-red); }
  .badge-core { fill: var(--sign-yellow); stroke: var(--sign-black); stroke-width: 2; }
  .badge-hours { fill: var(--sign-black); font-weight: 900; font-size: 206px; }
  .badge-unit { fill: var(--sign-red); font-weight: 900; font-size: 80px; }
  .badge-caption { fill: var(--sign-black); font-weight: 700; font-size: 30px; }
  .camera-area { fill: url(#camera-tone); }
  .notice-line { fill: var(--sign-black); font-weight: 700; font-size: 36px; }
  .footer-text { fill: var(--sign-white); font-weight: 700; font-size: 38px; }
</style>
</head>
<body>
<svg class="sign" viewBox="0 0 793 792" preserveAspectRatio="none" xmlns="http://www.w3.org/2000/svg">
  <defs>
    <linearGradient id="camera-tone" x1="0" y1="0" x2="1" y2="1">
      <stop offset="0" stop-color="var(--camera-dark)"/>
      <stop offset="1" stop-color="var(--camera-light)"/>
    </linearGradient>
  </defs>

  <g class="header">
    <rect class="header-band-edge" x="0" y="0" width="793" height="225"/>
    <rect class="header-band" x="0" y="31" width="793" height="162"/>
    <text class="header-title" x="397" y="167" text-anchor="middle" textLength="660" lengthAdjust="spacingAndGlyphs">WARNING</text>
  </g>

  <rect class="footer-band" x="0" y="714" width="793" height="78"/>

  <g class="camera" role="img" aria-label="Line drawing of a wall-mounted security camera with mounting bracket and cable">
    <rect class="camera-area" x="340" y="246" width="450" height="276" rx="40" ry="40"/>
  </g>

  <g class="badge">
    <circle class="badge-halo" cx="212" cy="530" r="242"/>
    <circle class="badge-ring" cx="212" cy="530" r="231"/>
    <circle class="badge-core" cx="212" cy="530" r="209"/>
    <text class="badge-hours" x="205" y="556" text-anchor="middle" textLength="234" lengthAdjust="spacingAndGlyphs">24</text>
    <text class="badge-unit" x="206" y="626" text-anchor="middle" textLength="226" lengthAdjust="spacingAndGlyphs">HOUR</text>
    <text class="badge-caption" x="202" y="666" text-anchor="middle" textLength="234" lengthAdjust="spacingAndGlyphs">SURVEILLANCE</text>
  </g>

  <g class="notice">
    <text class="notice-line" x="760" y="640" text-anchor="end" textLength="260" lengthAdjust="spacingAndGlyphs">All Suspicious</text>
    <text class="notice-line" x="760" y="688" text-anchor="end" textLength="348" lengthAdjust="spacingAndGlyphs">or Criminal Activity</text>
    <text class="footer-text" x="758" y="768" text-anchor="end" textLength="376" lengthAdjust="spacingAndGlyphs">WILL BE REPORTED!</text>
  </g>
</svg>
</body>
</html>
```